Bright Willow Wellness
Heal your Body Mind and Spirit
Bright Willow Wellness - Health
Creative Brief
Professional
Melora T. Grant, MSW, LSW
Health Consultant and Spiritual Counselor
Certifications: Feeling Map Form Key Spiritual Counseling
melora@brightwillowwellness.example
www.brightwillowwellness.example
Next appointment: _____________________________________
guest guest
where is the logo
mgrant417 mgrant417
Designers: Please only design for business cards, not stationary. Thanks...

```html
<!DOCTYPE html>
<html lang="en">
<head>
<meta charset="utf-8">
<title>Bright Willow Wellness – Stationery</title>
<link rel="stylesheet" href="https://fonts.googleapis.com/css2?family=Libre+Baskerville:ital,wght@0,400;1,400&family=Lato:wght@400;700&display=swap">
<style>
  :root {
    --navy: #1a2d5c;
    --teal: #2c7b98;
    --paper: #ffffff;
    --backdrop: #e8e9eb;
    --ink: #3a4150;
    --mute: #8a93a3;
  }
  * { box-sizing: border-box; margin: 0; padding: 0; }
  html, body { width: 1200px; height: 936px; overflow: hidden; background: var(--backdrop); }
  .stage { position: relative; width: 1200px; height: 936px; font-family: "Lato", sans-serif; color: var(--ink); }
  .sheet { position: absolute; background: var(--paper); box-shadow: 0 2px 6px rgba(0,0,0,0.12); overflow: hidden; }

  /* Thin corner brackets */
  .bracket { position: absolute; width: var(--c); height: var(--c); border: 0 solid var(--navy); }
  .bracket.tl { top: var(--i); left: var(--i); border-top-width: var(--w); border-left-width: var(--w); }
  .bracket.tr { top: var(--i); right: var(--i); border-top-width: var(--w); border-right-width: var(--w); }
  .bracket.bl { bottom: var(--i); left: var(--i); border-bottom-width: var(--w); border-left-width: var(--w); }
  .bracket.br { bottom: var(--i); right: var(--i); border-bottom-width: var(--w); border-right-width: var(--w); }

  .brand-name { font-family: "Libre Baskerville", serif; font-weight: 400; color: var(--navy); white-space: nowrap; }
  .tagline { font-family: "Lato", sans-serif; font-weight: 400; color: var(--teal); white-space: nowrap; letter-spacing: 0.04em; }

  /* Letterhead */
  .letterhead { left: 182px; top: 68px; width: 385px; height: 535px; --c: 34px; --i: 12px; --w: 2px; }
  .letterhead .lockup { position: absolute; left: 34px; top: 26px; }
  .letterhead .brand-name { font-size: 10px; }
  .letterhead .tagline { font-size: 5.5px; margin-top: 3px; }
  .letterhead .contact { position: absolute; right: 34px; top: 26px; font-size: 5.5px; line-height: 1.6; color: var(--mute); text-align: right; }

  /* Presentation folder */
  .folder { left: 633px; top: 38px; width: 448px; height: 572px; --c: 52px; --i: 16px; --w: 3px; }
  .folder .centre { position: absolute; left: 0; right: 0; top: 262px; text-align: center; }
  .folder .brand-name { display: block; font-size: 24px; }
  .folder .tagline { display: block; font-size: 12px; margin-top: 10px; }

  /* Business cards */
  .card { left: 43px; width: 172px; height: 104px; --c: 14px; --i: 6px; --w: 1.2px; }
  .card-front { top: 658px; }
  .card-back { top: 780px; }
  .card .lockup { position: absolute; left: 14px; top: 13px; }
  .card .brand-name { font-size: 6.6px; }
  .card .tagline { font-size: 3.8px; margin-top: 2px; }
  .card-front .details { position: absolute; left: 14px; top: 40px; font-size: 4.6px; line-height: 1.55; color: var(--ink); }
  .card-front .details strong { color: var(--navy); font-size: 5.4px; }
  .card-back .fields { position: absolute; left: 14px; top: 16px; right: 16px; font-size: 4.8px; color: var(--ink); }
  .card-back .field { display: flex; gap: 4px; margin-bottom: 12px; }
  .card-back .field span:last-child { flex: 1; border-bottom: 0.6px solid var(--mute); }

  /* Envelopes */
  .envelope { top: 673px; width: 418px; height: 203px; --c: 28px; --i: 10px; --w: 2px; }
  .envelope-front { left: 268px; }
  .envelope-front .lockup { position: absolute; left: 24px; top: 24px; }
  .envelope-front .brand-name { font-size: 8px; }
  .envelope-front .tagline { font-size: 4.6px; margin-top: 2px; }
  .envelope-back { left: 737px; }
  .envelope-back .flap { position: absolute; left: 0; top: 0; width: 100%; height: 88px; background: var(--navy); }
  .envelope-back .web { position: absolute; left: 0; right: 0; top: 22px; text-align: center; color: #fff; font-family: "Lato", sans-serif; font-size: 7px; letter-spacing: 0.2em; text-transform: uppercase; }
</style>
</head>
<body>
<main class="stage">

  <section class="sheet letterhead" aria-label="Letterhead">
    <span class="bracket tl"></span><span class="bracket tr"></span><span class="bracket bl"></span><span class="bracket br"></span>
    <div class="lockup">
      <div class="brand-name">Bright Willow Wellness</div>
      <div class="tagline">Heal your Body Mind and Spirit</div>
    </div>
    <div class="contact">
      <div>Melora T. Grant</div>
      <div>melora@brightwillowwellness.example</div>
      <div>www.brightwillowwellness.example</div>
    </div>
  </section>

  <section class="sheet folder" aria-label="Presentation folder">
    <span class="bracket tl"></span><span class="bracket tr"></span><span class="bracket bl"></span><span class="bracket br"></span>
    <div class="centre">
      <span class="brand-name">Bright Willow Wellness</span>
      <span class="tagline">Heal your Body Mind and Spirit</span>
    </div>
  </section>

  <section class="sheet card card-front" aria-label="Business card front">
    <span class="bracket tl"></span><span class="bracket tr"></span><span class="bracket bl"></span><span class="bracket br"></span>
    <div class="lockup">
      <div class="brand-name">Bright Willow Wellness</div>
      <div class="tagline">Heal your Body Mind and Spirit</div>
    </div>
    <div class="details">
      <strong>Melora T. Grant</strong><br>
      Health Consultant and Spiritual Counselor<br>
      melora@brightwillowwellness.example<br>
      www.brightwillowwellness.example
    </div>
  </section>

  <section class="sheet card card-back" aria-label="Business card back">
    <span class="bracket tl"></span><span class="bracket tr"></span><span class="bracket bl"></span><span class="bracket br"></span>
    <div class="fields">
      <div class="field"><span>Next appointment:</span><span></span></div>
      <div class="field"><span>Date:</span><span></span></div>
      <div class="field"><span>Time:</span><span></span></div>
      <div class="field"><span>Notes:</span><span></span></div>
    </div>
  </section>

  <section class="sheet envelope envelope-front" aria-label="Envelope front">
    <span class="bracket tl"></span><span class="bracket tr"></span><span class="bracket bl"></span><span class="bracket br"></span>
    <div class="lockup">
      <div class="brand-name">Bright Willow Wellness</div>
      <div class="tagline">Heal your Body Mind and Spirit</div>
    </div>
  </section>

  <section class="sheet envelope envelope-back" aria-label="Envelope back">
    <div class="flap"></div>
    <div class="web">www.brightwillowwellness.example</div>
  </section>

</main>
</body>
</html>
```